Business card for different employees

A professional new updated design incorporating our current business's color themes and styles such as our on-site service trucks decals included in pictures attached. Our current business card is very simple and not professionally designed. We are a small family business but want a professional corporate look.

Target Market(s)

Cards to be handed out to new customers , corperate meetings. For our on site service operators.

Industry/Entity Type

Hydraulic

Contact Information for Business Card

Address, website, phone number, email, logo.
slogan - "Industry chosen hose and fittings provider".
24/7 on-site service , supply and hose management
Experienced , indpendant , family owned

Font styles to use
Sans Serif

Requirements
Must have
• Easily editable so that I can add different names and different roles for employees etc.
Nice to have
• Freedom with colour doesn't necessarily have to be blue but that is our company colour theme with trucks and logo so makes sense for the card to have blue like the trucks.

```html
<!DOCTYPE html>
<html lang="en">
<head>
<meta charset="utf-8">
<title>Meridian Hose and Fittings – Business Card</title>
<link href="https://fonts.googleapis.com/css2?family=Arimo:wght@400;700&family=Open+Sans:wght@700&display=swap" rel="stylesheet">
<style>
  :root {
    --backdrop: #0b0b0c;
    --card: #2b2b2e;
    --card-edge: #1f3fd6;
    --brand-blue: #1f3fd6;
    --text-light: #e6e6e8;
    --text-muted: #b9b9bd;
    --rule: #56565b;
    --name-grey: #5f5f64;
  }
  * { margin: 0; padding: 0; box-sizing: border-box; }
  html, body { width: 1200px; height: 820px; overflow: hidden; }
  body {
    background: var(--backdrop);
    font-family: "Arimo", Arial, sans-serif;
    color: var(--text-light);
    position: relative;
  }
  .card {
    position: absolute;
    top: 256px;
    width: 540px;
    height: 308px;
    background: var(--card);
    border-bottom: 4px solid var(--card-edge);
    border-right: 2px solid var(--card-edge);
    box-shadow: 0 18px 40px rgba(0,0,0,.6);
  }
  .card--front { left: 40px; }
  .card--back { left: 620px; }

  /* front */
  .brand {
    position: absolute; top: 38px; left: 90px;
    display: flex; align-items: center; gap: 14px;
  }
  .brand__dot {
    width: 46px; height: 46px; border-radius: 50%;
    background: var(--brand-blue);
  }
  .brand__name {
    font-family: "Open Sans", Arial, sans-serif;
    font-weight: 700; font-size: 22px; letter-spacing: .5px;
    color: var(--text-light); text-transform: uppercase;
    line-height: 1.1;
  }
  .slogan {
    position: absolute; top: 104px; left: 150px;
    font-family: "Open Sans", Arial, sans-serif;
    font-weight: 700; font-size: 10.5px; letter-spacing: .3px;
    text-transform: uppercase; color: var(--text-light);
  }
  .divider {
    position: absolute; top: 146px; left: 200px; width: 300px;
    height: 1px; background: var(--rule);
  }
  .person { position: absolute; top: 166px; left: 36px; }
  .person__name {
    color: var(--brand-blue); font-weight: 700; font-size: 17px;
    text-transform: uppercase; letter-spacing: .4px;
  }
  .person__role { font-size: 15px; margin-top: 2px; }
  .contacts {
    position: absolute; top: 222px; left: 36px;
    list-style: none; font-size: 15px;
  }
  .contacts li { display: flex; align-items: center; gap: 8px; height: 22px; }
  .contacts svg { width: 15px; height: 15px; flex: none; }
  .address {
    position: absolute; top: 170px; right: 36px;
    font-size: 15px; line-height: 1.35; text-align: left;
  }

  /* back */
  .back-name {
    position: absolute; top: 84px; left: 40px; width: 240px;
    font-family: "Open Sans", Arial, sans-serif;
    font-weight: 700; font-size: 30px; line-height: 1.15;
    letter-spacing: 1px; text-transform: uppercase;
    color: var(--name-grey);
  }
  .services {
    position: absolute; top: 96px; right: 34px;
    text-align: center; font-size: 14px; line-height: 1.3;
    color: var(--text-muted);
  }
  .services__lead {
    font-weight: 700; color: var(--text-light);
    text-transform: uppercase; font-size: 15px;
  }
</style>
</head>
<body>

  <section class="card card--front" aria-label="Business card front">
    <div class="brand">
      <span class="brand__dot"></span>
      <span class="brand__name">Meridian<br>Hose and Fittings</span>
    </div>
    <p class="slogan">Industry chosen hose and fittings provider</p>
    <span class="divider"></span>

    <div class="person">
      <p class="person__name">Daniel Brooks</p>
      <p class="person__role">Managing Director</p>
    </div>

    <ul class="contacts">
      <li>
        <svg viewBox="0 0 16 16" aria-hidden="true"><rect x="1" y="1" width="14" height="14" rx="2" fill="none" stroke="#1f3fd6" stroke-width="1.4"/><path d="M5 4l2 2-1 1.2c.6 1.3 1.5 2.2 2.8 2.8L10 9l2 2-1.3 1.3C7.5 12 4 8.5 3.7 5.3z" fill="#1f3fd6"/></svg>
        <span>0400 123 456</span>
      </li>
      <li>
        <svg viewBox="0 0 16 16" aria-hidden="true"><rect x="1" y="3" width="14" height="10" fill="#1f3fd6"/><path d="M1 3l7 6 7-6" fill="none" stroke="#2b2b2e" stroke-width="1.3"/></svg>
        <span>info@meridianhose.com</span>
      </li>
      <li>
        <svg viewBox="0 0 16 16" aria-hidden="true"><circle cx="8" cy="8" r="7" fill="#1f3fd6"/><path d="M1 8h14M8 1c-3 3.5-3 10.5 0 14M8 1c3 3.5 3 10.5 0 14" fill="none" stroke="#2b2b2e" stroke-width="1"/></svg>
        <span>www.meridianhose.com.au</span>
      </li>
    </ul>

    <p class="address">421, Address line here<br>Country Name, 45452</p>
  </section>

  <section class="card card--back" aria-label="Business card back">
    <p class="back-name">Meridian<br>Hose and<br>Fittings</p>
    <div class="services">
      <p class="services__lead">24/7 On-site Service</p>
      <p>Supply and Hose<br>Management</p>
      <p>Experienced, Indpendant<br>Family Owned</p>
    </div>
  </section>

</body>
</html>
```